New Website for consulting company

We need a completely new design for our company web site: www.morvane-advisory.ch (please do not use it as a reference. We want something completely different.)
We are a consulting company and therefore our team is our key ressource together with our skills.
This site will be german in the first place. It will be the webmasters job to create it multilingual.
The website should be rather eccentric but still informative.
For colors and logo please refer to attached Logodefinition.pdf. The colored horizontal logo should be somehow used for the website but doesn't need to be extremely prominent. You can choose every color for the design but the logo must be somehow embedded in original colors and the green should be integrated for the site.
Please keep in mind that it should also work for mobile devices so the webmaster will have to create a responsive website out of the submitted design.
The main Page should be a one pager with different layout blocks directly accessible via top sticky menubar.:
- AKTEURE (team), gallery, people centric with images of member and expandable description box, plus skills abstract list (name & description). See attached mockups to support the explaining (do not take it as a reference).
- ÜBER UNS (mission), Description of companies vision, mission, competences etc.
- ... according to the menu bar
We would like to have at least 3 different block layouts to fill with content for the one pager site:
1. Team is the most important and the least generic one
2. Big picture less text
3. Multiple smaller pictures multiple text blocks
4. Hardly any picture text centric
The page should communicate competence in what we are doing, quality and not least youth and freshness.
See Attachements:
- Logodefinition.pdf: Logo definition containing definition of color of the logo.
- mockup_Website_mock1.png: These should give you an impression of how it is meant to have layouted blocks

```html
<!DOCTYPE html>
<html lang="en">
<head>
<meta charset="utf-8">
<title>Morvane Advisory – Website Design</title>
<link href="https://fonts.googleapis.com/css2?family=Lato:ital,wght@0,300;0,400;0,700;0,900;1,300;1,400&display=swap" rel="stylesheet">
<style>
  :root {
    --green: #7dc242;
    --ink: #1e1e1e;
    --text: #555555;
    --muted: #9d9d9d;
    --faint: #cfcfcf;
    --page: #ffffff;
    --stage: #e9eaec;
    --photo-light: #e6e4e1;
    --photo-suit: #3b4150;
    --photo-room-a: #8a6a52;
    --photo-room-b: #cbb8a4;
  }
  * { box-sizing: border-box; margin: 0; padding: 0; }
  html, body { width: 1200px; height: 800px; overflow: hidden; }
  body {
    background: var(--stage);
    font-family: "Lato", sans-serif;
    color: var(--ink);
    position: relative;
  }

  .screen {
    position: absolute;
    background: var(--page);
    box-shadow: 0 2px 10px rgba(0,0,0,0.08);
    overflow: hidden;
  }

  /* Desktop: team section */
  .team-section { left: 24px; top: 24px; width: 780px; height: 372px; padding: 26px 34px; }
  .team-section__title {
    font-weight: 300; font-size: 32px; letter-spacing: 1px;
    color: var(--faint); text-transform: uppercase;
  }
  .team-section__intro { display: flex; gap: 60px; margin-top: 10px; }
  .team-section__intro p {
    flex: 1; font-style: italic; font-weight: 300;
    font-size: 11px; line-height: 1.45; color: var(--muted);
  }
  .team-gallery { display: flex; gap: 34px; margin-top: 22px; padding-left: 20px; }
  .team-member { position: relative; width: 200px; height: 178px; }
  .team-member__photo {
    width: 100%; height: 100%;
    background: linear-gradient(180deg, var(--photo-light) 0%, var(--photo-light) 30%, var(--photo-suit) 31%, #2d3240 100%);
    border-radius: 2px;
  }
  .team-member__photo--light {
    background: linear-gradient(180deg, var(--photo-light) 0%, var(--photo-light) 30%, #a9c1dc 31%, #7f9ab8 100%);
  }
  .name-tag {
    position: absolute; left: -14px; bottom: 22px;
    background: var(--green); color: #fff;
    font-size: 10px; font-weight: 400; letter-spacing: 0.6px; text-transform: uppercase;
    padding: 10px 14px; width: 150px;
    display: flex; justify-content: space-between; align-items: center;
  }

  /* Desktop: member detail */
  .member-detail { left: 24px; top: 412px; width: 780px; height: 364px; padding: 0 34px; }
  .member-strip { display: flex; gap: 14px; }
  .member-strip__item { width: 140px; }
  .member-strip__photo {
    height: 34px;
    background: linear-gradient(180deg, #2f3442, #3b4150);
  }
  .member-strip__role {
    margin-top: 4px; font-size: 8px; font-weight: 700;
    color: var(--green); text-transform: uppercase; letter-spacing: 0.4px;
  }
  .member-detail__body { display: flex; gap: 26px; margin-top: 18px; }
  .member-detail__text { flex: 1; }
  .member-detail__icon { display: block; margin-bottom: 6px; }
  .member-detail__name { font-size: 20px; font-weight: 900; text-transform: uppercase; margin-bottom: 6px; }
  .member-detail__text p { font-size: 9.5px; line-height: 1.5; color: var(--text); margin-bottom: 9px; }
  .member-detail__aside { width: 170px; position: relative; }
  .member-detail__photo {
    width: 170px; height: 220px;
    background: linear-gradient(180deg, #f1efec 0%, #f1efec 28%, var(--photo-suit) 29%, #2b303c 100%);
  }
  .further-button {
    position: absolute; right: 0; top: 248px;
    background: var(--green); color: #fff;
    font-size: 9px; font-weight: 700; text-transform: uppercase; letter-spacing: 0.5px;
    padding: 7px 10px; display: flex; gap: 8px; align-items: center;
  }

  /* Mobile: home view */
  .mobile-home { left: 848px; top: 98px; width: 330px; height: 604px; }
  .mobile-header {
    height: 64px; display: flex; align-items: center; justify-content: space-between;
    padding: 0 14px; border-bottom: 1px solid #eee;
  }
  .brand { display: flex; align-items: center; gap: 8px; }
  .brand__square { width: 26px; height: 26px; background: var(--green); }
  .brand__name { font-size: 15px; font-weight: 700; color: var(--green); }
  .menu-toggle {
    width: 40px; height: 40px; border: 2px solid var(--green);
    display: flex; align-items: center; justify-content: center;
  }
  .mobile-hero {
    height: 330px;
    background: linear-gradient(160deg, var(--photo-room-b) 0%, var(--photo-room-a) 45%, #3f5a4a 100%);
  }
  .mobile-claim {
    margin: -70px 18px 0; position: relative;
    background: var(--page); padding: 14px 16px 12px;
  }
  .mobile-claim__title { font-size: 24px; font-weight: 400; line-height: 1.1; color: var(--ink); }
  .mobile-claim__title strong { color: var(--green); font-weight: 900; }
  .mobile-claim p { margin-top: 10px; font-size: 9.5px; line-height: 1.5; color: var(--text); }
  .read-more {
    display: block; text-align: right; margin-top: 10px;
    font-size: 9px; font-weight: 700; color: var(--green);
  }
</style>
</head>
<body>

  <section class="screen team-section">
    <h1 class="team-section__title">Get to know us</h1>
    <div class="team-section__intro">
      <p>We are an interdisciplinary and innovative team of specialists with training in computer science and business. For many years we operate in and on projects of all types and content, and possess an optimal combination of knowledge and experience.</p>
      <p>Our employees have a high standard of training (computer science and business administration at least technical college level) and are certified in many subject areas, for example in requirements engineering, ITIL and course in project management.</p>
    </div>
    <div class="team-gallery">
      <article class="team-member">
        <div class="team-member__photo" role="img" aria-label="Portrait of a smiling consultant in a dark suit and tie"></div>
        <span class="name-tag">Matthias Steiner
          <svg width="10" height="8" viewBox="0 0 10 8"><path d="M0 4h8M5 1l3 3-3 3" stroke="#fff" stroke-width="1.3" fill="none"/></svg>
        </span>
      </article>
      <article class="team-member">
        <div class="team-member__photo team-member__photo--light" role="img" aria-label="Portrait of a consultant in a light blue shirt with arms crossed"></div>
        <span class="name-tag">Lukas Brenner
          <svg width="10" height="8" viewBox="0 0 10 8"><path d="M0 4h8M5 1l3 3-3 3" stroke="#fff" stroke-width="1.3" fill="none"/></svg>
        </span>
      </article>
      <article class="team-member">
        <div class="team-member__photo" role="img" aria-label="Portrait of a consultant in a dark suit"></div>
      </article>
    </div>
  </section>

  <section class="screen member-detail">
    <div class="member-strip">
      <div class="member-strip__item"><div class="member-strip__photo" role="img" aria-label="Team member portrait, cropped"></div><div class="member-strip__role">Project Manager</div></div>
      <div class="member-strip__item"><div class="member-strip__photo" role="img" aria-label="Team member portrait, cropped"></div><div class="member-strip__role">Project Manager</div></div>
      <div class="member-strip__item"><div class="member-strip__photo" role="img" aria-label="Team member portrait, cropped"></div><div class="member-strip__role">Project Manager</div></div>
    </div>
    <div class="member-detail__body">
      <div class="member-detail__text">
        <svg class="member-detail__icon" width="18" height="15" viewBox="0 0 18 15"><rect x="1" y="4" width="16" height="10" fill="none" stroke="#c4c4c4" stroke-width="1.2"/><path d="M6 4V1.5h6V4" fill="none" stroke="#c4c4c4" stroke-width="1.2"/></svg>
        <h2 class="member-detail__name">Matthias Steiner</h2>
        <p>My professional career began at the Alpine Rail Services in the Directorate freight (today ARS Freight), where I have a project assistant in the computer science project worked "Freight Tracking Suite / FTS". My interest in technical computer science led to the exchange of Varden Data (now Norvatek Systems) in the first-level support of ARS. Then I worked as a system engineer, the customer platform K400 (switch job ARS).</p>
        <p>My love for project business I could for the Nordline Operations Center as a technical project manager in the customer project "IT harmonization of the canton" and later in the ASP environment of data center Kantonet computer science AG maintain.</p>
        <p>ITIL V3 and IT Service Management as a discipline have asked me in recent years as a consultant and project manager in customer projects for the introduction of service management solutions and encouraged.</p>
        <p>I am pleased to be able to offer you my commitment and my broad knowledge of computer science as Morvane Advisory. More can be found on the following pages and in detail in the CV that you here can be requested.</p>
      </div>
      <div class="member-detail__aside">
        <div class="member-detail__photo" role="img" aria-label="Full portrait of the consultant in a dark suit, hands in pockets"></div>
        <span class="further-button">Further
          <svg width="9" height="7" viewBox="0 0 10 8"><path d="M0 4h8M5 1l3 3-3 3" stroke="#fff" stroke-width="1.3" fill="none"/></svg>
        </span>
      </div>
    </div>
  </section>

  <section class="screen mobile-home">
    <header class="mobile-header">
      <div class="brand"><span class="brand__square"></span><span class="brand__name">Morvane Advisory</span></div>
      <div class="menu-toggle">
        <svg width="18" height="14" viewBox="0 0 18 14"><path d="M0 1h18M0 7h18M0 13h18" stroke="#7dc242" stroke-width="2.4"/></svg>
      </div>
    </header>
    <div class="mobile-hero" role="img" aria-label="Smiling consultant with glasses and a green sweater, arms crossed, in a warm office"></div>
    <div class="mobile-claim">
      <h2 class="mobile-claim__title"><strong>Your success</strong> is our motivation.</h2>
      <p>We think we are strategically and networked, methodical and structured. To get to the point, our solutions are perfectly matched to your needs and goals. And all we continue to learn every day, so our clients always receive a regular, fresh view of their work.</p>
      <a class="read-more">» Read more</a>
    </div>
  </section>

</body>
</html>
```